Kestrel Works Business Cards

This job is for the design of a business card.
I would like to review the design in 2x colour tones to choose from black and white inverted.
EG:
Black with white logo and white with black logo on BACK
White with black text on front and black with white text options
PRINTING DIMENSIONS: 4.5 x 8.5cm
Complete design will need to be provided in ready to print format with bleed lines
Target Market(s)
The audience of my business are people in the trade industry.
It will be also used for general networking with trades people and possible future clients.
I want to be represented as a professional, dynamic, creative and personable operator.
The card should reflect style, taste, experience, professionalism.
Industry/Entity Type
Business
Requirements
Must have
- BACK CONTENT:
- Logo in white and black background and vice versa with WHITE card and black logo review samples.
- FRONT CARD CONTENT:
- Name: Morgan Telvane
- Director
- Phone: 0438 216 947
- Email: morgan@kestrelworks.com.au
- Web: kestrelworks.com.au
- LICENCE #: KT-R 72158
Nice to have
- Possibly a textured background design on rear as a pose to a solid black
- Possibly adding a blue or orange discreet colour tone (possibly for email, phone abbreviated letter or symbols).

```html
<!DOCTYPE html>
<html lang="en">
<head>
<meta charset="utf-8">
<title>Kestrel Works Business Cards</title>
<link rel="stylesheet" href="https://fonts.googleapis.com/css2?family=Questrial&display=swap">
<style>
  :root {
    --backdrop: #2b2420;
    --ink: #0b0b0b;
    --paper: #ffffff;
    --band: #d9d9d9;
    --band-edge: #bcbcbc;
    --accent: #2b58b0;
    --text: #141414;
    --muted: #555555;
    --shadow: rgba(0, 0, 0, 0.55);
  }
  html, body {
    margin: 0;
    padding: 0;
    width: 1200px;
    height: 873px;
    overflow: hidden;
    background: var(--backdrop);
    font-family: "Questrial", "Helvetica Neue", Arial, sans-serif;
  }
  .canvas {
    position: relative;
    width: 1200px;
    height: 873px;
  }
  .card {
    position: absolute;
    width: 480px;
    height: 254px;
    box-shadow: 0 6px 18px var(--shadow);
    overflow: hidden;
  }

  /* Back of card: black field with light base band */
  .card-back {
    left: 90px;
    top: 130px;
    background: var(--ink);
  }
  .card-back .base-band {
    position: absolute;
    left: 0;
    right: 0;
    bottom: 0;
    height: 62px;
    background: linear-gradient(180deg, var(--paper) 0%, var(--band) 100%);
    border-top: 1px solid var(--band-edge);
  }
  .card-back .brand-name {
    position: absolute;
    right: 32px;
    bottom: 70px;
    margin: 0;
    color: var(--paper);
    font-size: 44px;
    font-weight: 400;
    letter-spacing: 1px;
    line-height: 1;
    text-transform: uppercase;
    white-space: nowrap;
  }

  /* Front of card: black spine strip with contact details */
  .card-front {
    left: 625px;
    top: 512px;
    background: var(--paper);
  }
  .card-front .spine {
    position: absolute;
    left: 0;
    top: 0;
    bottom: 0;
    width: 72px;
    background: var(--ink);
    display: flex;
    align-items: center;
    justify-content: center;
  }
  .card-front .spine-name {
    margin: 0;
    color: var(--paper);
    font-size: 23px;
    font-weight: 400;
    line-height: 1;
    letter-spacing: 0.5px;
    text-transform: uppercase;
    white-space: nowrap;
    writing-mode: vertical-rl;
    transform: rotate(180deg);
  }
  .holder {
    position: absolute;
    right: 38px;
    top: 26px;
    margin: 0;
    text-align: right;
  }
  .holder-name {
    display: block;
    font-size: 22px;
    line-height: 28px;
    color: var(--text);
  }
  .holder-role {
    display: block;
    font-size: 14px;
    line-height: 20px;
    letter-spacing: 2px;
    text-transform: uppercase;
    color: var(--muted);
  }
  .contact-list {
    position: absolute;
    right: 38px;
    top: 116px;
    margin: 0;
    padding: 0;
    list-style: none;
    text-align: right;
    font-size: 20px;
    line-height: 32px;
    color: var(--text);
  }
  .contact-list .label {
    color: var(--accent);
    text-transform: uppercase;
  }
</style>
</head>
<body>
  <main class="canvas">
    <section class="card card-back" aria-label="Card back">
      <div class="base-band"></div>
      <h1 class="brand-name">Kestrel Works</h1>
    </section>

    <section class="card card-front" aria-label="Card front">
      <div class="spine">
        <p class="spine-name">Kestrel Works</p>
      </div>
      <p class="holder">
        <span class="holder-name">Morgan Telvane</span>
        <span class="holder-role">Director</span>
      </p>
      <ul class="contact-list">
        <li><span class="label">Mobile:</span> 0438 216 947</li>
        <li><span class="label">Email:</span> morgan@kestrelworks.com.au</li>
        <li><span class="label">Web:</span> kestrelworks.com.au</li>
        <li><span class="label">Licence No.:</span> KT-R 72158</li>
      </ul>
    </section>
  </main>
</body>
</html>
```